Burn Cream

We need to develop a (1) tube and (2) carton design. For a Lidocaine 2.5% burn cream.

This is a topical application cream. KALVIO is the Product Name. 1 oz.

```html
<!DOCTYPE html>
<html lang="en">
<head>
<meta charset="utf-8">
<title>KALVIO Burn Cream – Tube Label</title>
<link rel="stylesheet" href="https://fonts.googleapis.com/css2?family=Montserrat:wght@500;700&display=swap">
<style>
  :root {
    --stage-blue: #0f3f8c;
    --label-navy: #17205a;
    --label-navy-deep: #0f1645;
    --stripe: #3a4f8f;
    --flame-core: #ffcf4a;
    --flame-mid: #f08a1c;
    --flame-edge: #a8330c;
    --ice-light: #eaf6ff;
    --ice-mid: #9fd0f2;
    --ice-deep: #2a6fc4;
    --ring-gold: #f2b43a;
    --name-white: #ffffff;
    --strength-teal: #4fc3c9;
  }
  html, body {
    margin: 0;
    padding: 0;
    overflow: hidden;
  }
  body {
    width: 1200px;
    height: 784px;
    background: var(--stage-blue);
    font-family: "Montserrat", sans-serif;
  }
  .canvas {
    position: relative;
    width: 1200px;
    height: 784px;
  }
  .tube-label {
    position: absolute;
    left: 100px;
    top: 262px;
    width: 1000px;
    height: 260px;
    background: linear-gradient(180deg, var(--label-navy) 0%, var(--label-navy-deep) 100%);
    overflow: hidden;
  }
  .flame-art {
    position: absolute;
    left: 60px;
    top: 20px;
    width: 470px;
    height: 220px;
    background: radial-gradient(ellipse at 70% 45%, var(--flame-core) 0%, var(--flame-mid) 35%, var(--flame-edge) 62%, rgba(23, 32, 90, 0) 78%);
  }
  .ice-art {
    position: absolute;
    right: 0;
    top: 0;
    width: 330px;
    height: 260px;
    background: linear-gradient(100deg, rgba(23, 32, 90, 0) 0%, var(--ice-deep) 30%, var(--ice-mid) 62%, var(--ice-light) 100%);
  }
  .bottom-stripe {
    position: absolute;
    left: 0;
    right: 0;
    top: 222px;
    height: 6px;
    background: var(--stripe);
  }
  .brand-seal {
    position: absolute;
    left: 430px;
    top: 20px;
    width: 220px;
    height: 220px;
  }
  .brand-seal svg {
    position: absolute;
    inset: 0;
  }
  .brand-name {
    position: absolute;
    left: 0;
    right: 0;
    top: 92px;
    margin: 0;
    text-align: center;
    font-weight: 700;
    font-size: 40px;
    letter-spacing: 2px;
    color: var(--name-white);
  }
  .strength {
    position: absolute;
    left: 0;
    right: 0;
    top: 68px;
    margin: 0;
    text-align: center;
    font-weight: 500;
    font-size: 13px;
    letter-spacing: 0.5px;
    color: var(--strength-teal);
  }
</style>
</head>
<body>
  <main class="canvas">
    <section class="tube-label">
      <div class="flame-art" role="img" aria-label="Burst of orange and yellow flames"></div>
      <div class="ice-art" role="img" aria-label="Shattered ice cubes and frosty crystals"></div>
      <div class="bottom-stripe"></div>
      <div class="brand-seal">
        <svg width="220" height="220" viewBox="0 0 220 220" aria-hidden="true">
          <circle cx="110" cy="110" r="104" fill="var(--label-navy-deep)" stroke="var(--ring-gold)" stroke-width="5"/>
        </svg>
        <p class="strength">Lidocaine 2.5%</p>
        <h1 class="brand-name">KALVIO</h1>
      </div>
    </section>
  </main>
</body>
</html>
```